modern design for software startup

We need a website design. We are a software company developing a cruise management system for cruise ships. We don't want or need something elaborate. In fact, we don't want to show specifics of our products because they are under development and we do not want our competitors to know too much. We want to focus on ideals and principals of our company and hint at what we are doing.

Target Market(s)

cruise lines

Industry/Entity Type

Software

Coding

Coded - Design and coding required

Number of Pages Required

1 page

Font styles to use
Sans Serif

Colors
7f7f7f
5c5c5c

Requirements
Must have
• background pictures of cruise ships, ports, ocean, some developers working on computers in brown and white and fuzzy. can't show specific cruise lines. magazine like style. white text. links at bottom to facebook, twitter, instagram
• email link for investor/partner inquiries.
Nice to have
• Some inspirational quotes here and there. Not overpowering but subtle. content to be provided in text file.
• color schemes - we like the scheme in www.velmorquartet.com
• doesnt have to be exact but similar is good.

```html
<!DOCTYPE html>
<html lang="en">
<head>
<meta charset="utf-8">
<title>Nautilo Software</title>
<link rel="stylesheet" href="https://fonts.googleapis.com/css2?family=Roboto+Slab:wght@400;500&family=Roboto+Condensed:wght@400;700&family=Arimo:wght@400;700&display=swap">
<style>
  :root{
    --brand-blue:#0a5aa8;
    --link-blue:#1e9ad6;
    --icon-blue:#2a78c2;
    --nav-active:#0b4f95;
    --ink-dark:#333333;
    --title-grey:#5c5c5c;
    --body-grey:#7f7f7f;
    --gold:#a89a5c;
    --white:#ffffff;
    --wood-light:#d29a5f;
    --wood-mid:#b8773f;
    --wood-dark:#8a5128;
    --caption-band:rgba(62,130,200,.82);
    --arrow-bg:#3a3a3a;
  }
  *{margin:0;padding:0;box-sizing:border-box}
  html,body{width:1200px;height:829px;overflow:hidden;background:var(--white)}
  body{position:relative;font-family:"Arimo",Arial,sans-serif}

  .top-strip{position:absolute;left:0;top:0;width:1200px;height:41px}
  .top-strip__gold{position:absolute;left:0;top:0;width:570px;height:3px;background:var(--gold)}
  .top-strip__bar{position:absolute;right:0;top:0;width:635px;height:41px;background:var(--ink-dark);clip-path:polygon(0 0,100% 0,100% 100%,45px 100%)}
  .contact{position:absolute;top:0;height:41px;display:flex;align-items:center;color:var(--white);font-family:"Roboto Slab",serif;text-decoration:none}
  .contact--phone{left:684px;font-size:19px}
  .contact--mail{left:856px;font-size:16px}
  .contact svg{margin-right:9px;flex:none}

  .brand{position:absolute;left:98px;top:26px;display:flex;align-items:center;gap:9px}
  .brand__mark{width:20px;height:20px;border-radius:50%;background:var(--brand-blue);flex:none}
  .brand__name{font-family:"Roboto Condensed",sans-serif;font-weight:700;color:var(--brand-blue);line-height:1;text-align:center}
  .brand__name span{display:block}
  .brand__word{font-size:33px;letter-spacing:1px}
  .brand__sub{font-size:12px;letter-spacing:4px;margin-top:3px}

  .main-nav{position:absolute;top:64px;left:0;width:1200px}
  .main-nav a{position:absolute;font-family:"Roboto Slab",serif;font-size:15px;color:var(--link-blue);text-decoration:none;white-space:nowrap;padding:0 8px 7px}
  .main-nav a.is-active{color:var(--nav-active);font-weight:500;border-bottom:1px solid var(--nav-active)}

  .hero{position:absolute;left:0;top:102px;width:1200px;height:418px;background:linear-gradient(160deg,var(--wood-light) 0%,var(--wood-mid) 45%,var(--wood-light) 70%,var(--wood-dark) 100%)}
  .hero__arrow{position:absolute;top:179px;width:34px;height:30px;background:var(--arrow-bg);display:flex;align-items:center;justify-content:center}
  .hero__arrow--prev{left:7px}
  .hero__arrow--next{right:7px}
  .hero__caption{position:absolute;left:157px;top:304px;width:905px;height:43px;background:var(--caption-band);color:var(--white);font-family:"Roboto Condensed",sans-serif;font-size:22px;display:flex;align-items:center;justify-content:center}

  .features{position:absolute;left:0;top:505px;width:1200px}
  .feature{position:absolute;top:0;width:280px;text-align:center}
  .feature--about{left:82px}
  .feature--team{left:432px}
  .feature--planet{left:820px}
  .feature__icon{width:101px;height:101px;margin:0 auto;border-radius:50%;border:1.5px solid var(--link-blue);background:var(--white);display:flex;align-items:center;justify-content:center}
  .feature__title{margin-top:16px;font-family:"Roboto Condensed",sans-serif;font-weight:700;font-size:17.5px;color:var(--title-grey);white-space:nowrap}
  .feature__text{width:252px;margin:10px auto 0;font-size:13.8px;line-height:18px;color:var(--body-grey)}
  .feature__more{display:inline-block;margin-top:9px;font-family:"Roboto Condensed",sans-serif;font-size:15px;color:var(--ink-dark);text-decoration:none;border-bottom:1px solid var(--ink-dark);line-height:17px}

  .site-footer{position:absolute;left:0;top:789px;width:1200px;height:40px;background:var(--brand-blue);color:var(--white)}
  .follow{position:absolute;left:96px;top:0;height:40px;display:flex;align-items:center;font-family:"Arimo",sans-serif;font-weight:700;font-size:14px;letter-spacing:.3px}
  .social{display:flex;gap:9px;margin-left:22px}
  .social a{width:28px;height:28px;border-radius:50%;background:var(--white);border:2px solid #d8d8d8;display:flex;align-items:center;justify-content:center}
  .copyright{position:absolute;right:99px;top:0;height:40px;display:flex;align-items:center;font-size:14px}
</style>
</head>
<body>
  <header>
    <div class="top-strip">
      <div class="top-strip__gold"></div>
      <div class="top-strip__bar"></div>
      <a class="contact contact--phone">
        <svg width="28" height="28" viewBox="0 0 28 28"><circle cx="14" cy="14" r="12.5" fill="none" stroke="#fff" stroke-width="1.5"/><path d="M10 8c1-1 2 0 3 2s0 2-1 3c1 2 2 3 4 4 1-1 1-2 3-1s3 2 2 3c-1 2-3 2-5 1-3-2-5-4-7-7-1-2-1-4 1-5z" fill="#fff"/></svg>
        555-014-2200
      </a>
      <a class="contact contact--mail" href="mailto:inquiry@nautilosoftware.com">
        <svg width="19" height="14" viewBox="0 0 19 14"><rect width="19" height="14" rx="1.5" fill="#fff"/><path d="M1 1.5l8.5 6.5 8.5-6.5" fill="none" stroke="#333" stroke-width="1.5"/></svg>
        inquiry@nautilosoftware.com
      </a>
    </div>

    <div class="brand">
      <span class="brand__mark"></span>
      <span class="brand__name"><span class="brand__word">NAUTILO</span><span class="brand__sub">SOFTWARE</span></span>
    </div>

    <nav class="main-nav">
      <a class="is-active" style="left:511px">HOME</a>
      <a style="left:592px">OUR MISSION</a>
      <a style="left:726px">WHO WE ARE</a>
      <a style="left:857px">COMMITMENT</a>
      <a style="left:1002px">CONTACT US</a>
    </nav>
  </header>

  <section class="hero" role="img" aria-label="Photo of a team around a wooden table working on laptops, tablets and phones">
    <span class="hero__arrow hero__arrow--prev"><svg width="10" height="14" viewBox="0 0 10 14"><path d="M8 2L3 7l5 5" fill="none" stroke="#fff" stroke-width="2.5"/></svg></span>
    <span class="hero__arrow hero__arrow--next"><svg width="10" height="14" viewBox="0 0 10 14"><path d="M2 2l5 5-5 5" fill="none" stroke="#fff" stroke-width="2.5"/></svg></span>
    <p class="hero__caption">We Are A Software Company Developing A Cruise Management System For Cruise Ships.</p>
  </section>

  <main class="features">
    <article class="feature feature--about">
      <div class="feature__icon">
        <svg width="58" height="58" viewBox="0 0 58 58" aria-hidden="true"><circle cx="29" cy="29" r="26" fill="var(--icon-blue)"/><circle cx="29" cy="17" r="4" fill="#fff"/><rect x="25" y="25" width="8" height="20" rx="2" fill="#fff"/></svg>
      </div>
      <h2 class="feature__title">About Nautilo Software</h2>
      <p class="feature__text">Lorem ipsum dolor sit amet, consectetuer adipiscing elit, sed diam nonummy nibh euod tincidunt ut laoreet dolore magna aliquam erat volutpat.</p>
      <a class="feature__more">Read More</a>
    </article>
    <article class="feature feature--team">
      <div class="feature__icon">
        <svg width="62" height="50" viewBox="0 0 62 50" aria-hidden="true"><rect x="9" y="6" width="44" height="30" rx="2" fill="var(--icon-blue)"/><rect x="13" y="10" width="36" height="22" fill="#7fc0ec"/><path d="M3 40h56l-4 6H7z" fill="var(--icon-blue)"/></svg>
      </div>
      <h2 class="feature__title">Who we Are</h2>
      <p class="feature__text">Lorem ipsum dolor sit amet, consectetuer adipiscing elit, sed diam nonummy nibh euod tincidunt ut laoreet dolore magna aliquam erat volutpat.</p>
      <a class="feature__more">Read More</a>
    </article>
    <article class="feature feature--planet">
      <div class="feature__icon">
        <svg width="60" height="60" viewBox="0 0 60 60" aria-hidden="true"><circle cx="30" cy="30" r="25" fill="#2aa0e0"/><g fill="none" stroke="#fff" stroke-width="2"><ellipse cx="30" cy="30" rx="11" ry="25"/><line x1="30" y1="5" x2="30" y2="55"/><line x1="5" y1="30" x2="55" y2="30"/><path d="M9 17h42M9 43h42"/></g></svg>
      </div>
      <h2 class="feature__title">Nautilo’s Commitment to our Planet</h2>
      <p class="feature__text">Lorem ipsum dolor sit amet, consectetuer adipiscing elit, sed diam nonummy nibh euod tincidunt ut laoreet dolore magna aliquam erat volutpat.</p>
      <a class="feature__more">Read More</a>
    </article>
  </main>

  <footer class="site-footer">
    <div class="follow">Follow Us On
      <div class="social">
        <a aria-label="Social profile">
          <svg width="14" height="14" viewBox="0 0 14 14"><path d="M2 2h10a1 1 0 0 1 1 1v6a1 1 0 0 1-1 1H6l-3 3v-3H2a1 1 0 0 1-1-1V3a1 1 0 0 1 1-1z" fill="#333"/></svg>
        </a>
        <a aria-label="Social profile">
          <svg width="14" height="14" viewBox="0 0 14 14"><g fill="#333"><circle cx="11" cy="3" r="2"/><circle cx="3" cy="7" r="2"/><circle cx="11" cy="11" r="2"/></g><path d="M11 3L3 7l8 4" fill="none" stroke="#333" stroke-width="1.3"/></svg>
        </a>
        <a aria-label="Social profile">
          <svg width="14" height="14" viewBox="0 0 14 14"><path d="M6 8l2-2M5 6L3.5 7.5a2.1 2.1 0 0 0 3 3L8 9M9 8l1.5-1.5a2.1 2.1 0 0 0-3-3L6 5" fill="none" stroke="#333" stroke-width="1.6" stroke-linecap="round"/></svg>
        </a>
      </div>
    </div>
    <p class="copyright">Copyright © 2016 Nautilo Software . All Rights Reserved.</p>
  </footer>
</body>
</html>
```